Business Card - high end, modern health care

Hey designers!

We need a double sided business card for the boutique, cutting edge physical therapy rehabilitation centre in Sydney's Northern Beaches.

With the most qualified physios in the area The Ridgeline Motion Clinic does what other physiotherapy practices do not, we take our time with our patients giving them longer appointments, better physios and therefor faster results!

We guarantee that the service people receive at TRMC will be unparalleled.

Hence we need a business card to reflect our modern, boutique, high end service. The final design needs to reflect that we are in a class of our own yet with the feel of beachside retreat.

Below I have attached our logo in both blue on white and white on blue. The exact colour is;
and the font that we have used in our logo is Tex Gyre Aventador.

I like the idea of the blue as the main colour as it is more eye catching and our signage onto the main road will be in this blue and in the interest of consistency across marketing the blue needs to be a part of the design. However I would appreciate a few designs onto a wooden background as this is a visual theme within the fitout of the practice.

The design needs to be of standard size (91x55mm).

Target Market(s)

We target people who have an end outcome in mind and those who have had poor experiences with other providers and ensure that everyone gets the care that they deserve with a premium service that is tailored to the individuals circumstances. As a premium service, the target market is highly educated, business and tech savvy with the additional target market of elderly people who have self funded their retirement and see value in paying for the best ongoing rehabilitation to maintain independence.

Industry/Entity Type

Physical Therapy

Contact Information for Business Card

Name, designation( Titled Musculoskeletal Physiotherapist... there will also be those in the company that have multiple designations ie 5 or 6 words long), phone number, email, facebook, instagram, address

Font styles to use
Sans Serif

Colors

Designer to choose colors to be used in the design.

Requirements
Must have
• Front - The logo as large as possible, blue or wooden theme, and all of the important details.
• Back - A blank space/lines on which to write appointment times (no "Appointment, date, time" etc.)
Nice to have
• facebook url
• logos for facebook and instagram
• Mini logos for the phone and email?

```html
<!DOCTYPE html>
<html lang="en">
<head>
<meta charset="utf-8">
<title>The Ridgeline Motion Clinic – Business Card</title>
<link href="https://fonts.googleapis.com/css2?family=Montserrat:wght@400;500;600;700&display=swap" rel="stylesheet">
<style>
  :root {
    --brand-blue: #1f5fae;
    --brand-blue-deep: #174a8c;
    --brand-blue-light: #2f78c4;
    --paper: #f4f5f7;
    --ink-white: #ffffff;
    --stage: #2a2b2e;
  }
  * { margin: 0; padding: 0; box-sizing: border-box; }
  html, body { width: 1200px; height: 900px; overflow: hidden; }
  body {
    background: var(--stage);
    font-family: "Montserrat", sans-serif;
    position: relative;
  }
  .card {
    position: absolute;
    left: 300px;
    width: 600px;
    height: 363px;
    border-radius: 22px;
    overflow: hidden;
  }
  .card-front { top: 56px; background: linear-gradient(150deg, var(--brand-blue-light) 0%, var(--brand-blue) 45%, var(--brand-blue-deep) 100%); color: var(--ink-white); }
  .card-back { top: 481px; background: var(--paper); color: var(--brand-blue); }

  .wordmark { position: absolute; display: flex; align-items: center; gap: 14px; }
  .wordmark-dot { width: 50px; height: 50px; border-radius: 50%; flex: none; }
  .wordmark-name { font-weight: 700; font-size: 30px; line-height: 1; letter-spacing: 0.5px; text-transform: uppercase; }
  .wordmark-sub { font-weight: 700; font-size: 17px; letter-spacing: 7px; text-transform: uppercase; margin-top: 6px; }

  .card-front .wordmark { left: 40px; top: 40px; }
  .card-front .wordmark-dot { background: var(--ink-white); }

  .holder { position: absolute; left: 40px; top: 150px; width: 330px; }
  .holder-name { font-weight: 700; font-size: 17px; letter-spacing: 1px; text-transform: uppercase; }
  .holder-title { font-size: 13px; margin-top: 4px; }
  .holder-rule { height: 1.5px; background: var(--ink-white); margin: 12px 0 12px; opacity: 0.9; }
  .contact-list { list-style: none; font-size: 12px; }
  .contact-list li { display: flex; align-items: center; gap: 10px; margin-bottom: 8px; white-space: nowrap; }
  .contact-icon { width: 18px; height: 18px; flex: none; }
  .social-dot { width: 14px; height: 14px; border-radius: 50%; border: 1.5px solid var(--ink-white); flex: none; }
  .contact-pair { display: flex; align-items: center; gap: 6px; margin-left: 8px; }

  .front-feature { position: absolute; right: 0; bottom: 0; width: 250px; height: 230px; }

  .back-feature { position: absolute; left: 0; top: 0; width: 250px; height: 363px; }
  .card-back .wordmark { left: 280px; top: 40px; }
  .card-back .wordmark-dot { background: var(--brand-blue); }
  .card-back .wordmark-name { font-size: 24px; }
  .card-back .wordmark-sub { font-size: 14px; letter-spacing: 6px; }
  .write-lines { position: absolute; left: 280px; top: 140px; width: 280px; }
  .write-line { height: 30px; border: 1px solid var(--brand-blue); border-radius: 15px; margin-bottom: 12px; }
  .back-url { position: absolute; left: 280px; top: 290px; font-size: 13px; font-weight: 500; }
  .back-edge { position: absolute; left: 0; right: 0; bottom: 0; height: 12px; background: var(--brand-blue); }
</style>
</head>
<body>

<section class="card card-front" aria-label="Business card front">
  <div class="wordmark">
    <span class="wordmark-dot"></span>
    <div>
      <div class="wordmark-name">The Ridgeline</div>
      <div class="wordmark-sub">Motion Clinic</div>
    </div>
  </div>

  <div class="holder">
    <div class="holder-name">Daniel Hartley</div>
    <div class="holder-title">Titled Musculoskeletal Physiotherapist</div>
    <div class="holder-rule"></div>
    <ul class="contact-list">
      <li>
        <svg class="contact-icon" viewBox="0 0 20 20"><circle cx="10" cy="10" r="9" fill="none" stroke="#fff" stroke-width="1.5"/><path d="M6.5 5.5l2 2-1 1.2c.6 1.4 1.6 2.4 3 3l1.2-1 2 2-1.2 1.3c-3.2-.4-6.4-3.6-6.8-6.8z" fill="#fff"/></svg>
        <span>0061 482 310</span>
        <span class="contact-pair"><span class="social-dot"></span>/<span class="social-dot"></span> ridgelinemotion</span>
      </li>
      <li>
        <svg class="contact-icon" viewBox="0 0 20 20"><circle cx="10" cy="10" r="9" fill="none" stroke="#fff" stroke-width="1.5"/><rect x="5.5" y="7" width="9" height="6.5" fill="none" stroke="#fff" stroke-width="1.2"/><path d="M5.5 7l4.5 3.5L14.5 7" fill="none" stroke="#fff" stroke-width="1.2"/></svg>
        <span>contact@ridgelinemotion.com.au</span>
      </li>
      <li>
        <svg class="contact-icon" viewBox="0 0 20 20"><circle cx="10" cy="10" r="9" fill="none" stroke="#fff" stroke-width="1.5"/><path d="M10 15s-3.5-3.6-3.5-6a3.5 3.5 0 0 1 7 0c0 2.4-3.5 6-3.5 6z" fill="#fff"/><circle cx="10" cy="9" r="1.2" fill="#1f5fae"/></svg>
        <span>1824 Harbour Lane, NSW 2100 Australia</span>
      </li>
    </ul>
  </div>

  <svg class="front-feature" viewBox="0 0 250 230" role="img" aria-label="Large brand emblem decoration area">
    <circle cx="250" cy="230" r="205" fill="none" stroke="#ffffff" stroke-width="4"/>
    <circle cx="250" cy="230" r="185" fill="#ffffff" opacity="0.95"/>
  </svg>
</section>

<section class="card card-back" aria-label="Business card back">
  <svg class="back-feature" viewBox="0 0 250 363" role="img" aria-label="Large brand emblem decoration area">
    <circle cx="20" cy="150" r="215" fill="#1f5fae"/>
    <circle cx="20" cy="150" r="190" fill="#2a6cb8"/>
  </svg>

  <div class="wordmark">
    <span class="wordmark-dot"></span>
    <div>
      <div class="wordmark-name">The Ridgeline</div>
      <div class="wordmark-sub">Motion Clinic</div>
    </div>
  </div>

  <div class="write-lines">
    <div class="write-line"></div>
    <div class="write-line"></div>
    <div class="write-line"></div>
  </div>

  <div class="back-url">www.ridgelinemotion.com.au</div>
  <div class="back-edge"></div>
</section>

</body>
</html>
```